Patient "menu"/catalog for IV Therapy spa

We have a "menu" that's basically just a bunch of Word documents explaining what we do and what's in each package, but it's weak. We had the pages laminated and bound at Paper Harbor and they look like crap. I also need to add information and be able to edit the pages. We HAVE to print the "catalog" with Printowl and want the size to be 5.5"x8.5" and glossy. We're imagining our logo on the front page, some "what to expect" and "what we're all about" info on the inside cover, and then each IV package and injection will have its own page. We can start with the copy that's currently on our menu, but we need to add some things to several of the pages. Things change all the time in this industry, and we're expanding regularly, so we have to have the ability to alter and reprint. I'm attaching some of the current files.

Target Market(s)

Current patients

Industry/Entity Type

Medical

Font styles to use
Other font styles liked:
• Whatever is on our bifold brochure would be fine.

Colors
0094D4
00A9DD
6FCCEA
C7EBF8
E9F6FB
00AB8E
00BBA5
67D7C9
C6EFE9
E9F9F6

Requirements
Must have
• 5.5:x8.5", printable at Printowl. Must be two-sided and editable by us for future changes
Nice to have
• Gotta be glossy and cool, but professional.
Should not have
• Stock images that we don't provide

```html
<!DOCTYPE html>
<html lang="en">
<head>
<meta charset="utf-8">
<title>Swift Renewal – IV Menu Spread</title>
<link href="https://fonts.googleapis.com/css2?family=Saira+Condensed:wght@600;700&family=Poppins:wght@400;600;700&display=swap" rel="stylesheet">
<style>
  :root{
    --blue-deep:#0094D4;
    --blue:#00A9DD;
    --blue-soft:#6FCCEA;
    --blue-pale:#C7EBF8;
    --blue-mist:#E9F6FB;
    --teal-deep:#00AB8E;
    --teal:#00BBA5;
    --teal-soft:#67D7C9;
    --teal-pale:#C6EFE9;
    --ink:#1d1f22;
    --body:#3b4046;
    --paper:#f7f8f9;
    --stage:#eef0f1;
  }
  *{box-sizing:border-box;margin:0;padding:0}
  html,body{width:1200px;height:900px;overflow:hidden;background:var(--stage)}
  body{font-family:"Poppins",sans-serif;color:var(--body)}
  .spread{position:absolute;left:82px;top:50px;width:1036px;height:800px;display:flex;box-shadow:0 6px 24px rgba(0,0,0,.12)}
  .page{position:relative;width:518px;height:800px;background:var(--paper);overflow:hidden}
  .page--left{border-right:1px solid #dfe3e6}
  .page__art{position:absolute;inset:0;width:100%;height:100%}
  .page__title{position:absolute;left:44px;top:30px;font-family:"Saira Condensed",sans-serif;font-weight:700;font-size:50px;letter-spacing:.5px;color:var(--ink);line-height:1}
  .page__title .accent{color:var(--teal)}
  .page__number{position:absolute;right:34px;width:24px;height:24px;border-radius:50%;background:var(--blue-pale);font-size:9px;font-weight:600;color:var(--ink);display:flex;align-items:center;justify-content:center}
  .page--left .page__number{top:212px}
  .page--right .page__number{top:290px}
  .brand{position:absolute;left:0;right:0;top:250px;display:flex;flex-direction:column;align-items:center;gap:4px}
  .brand__row{display:flex;align-items:center;gap:12px}
  .brand__dot{width:40px;height:40px;border-radius:50%;background:var(--blue-deep)}
  .brand__name{font-size:28px;font-weight:600;color:var(--blue-deep);line-height:1}
  .brand__tagline{font-size:11px;letter-spacing:2px;color:var(--body);margin-left:52px}
  .about{position:absolute;left:48px;right:44px;top:330px;font-size:9.6px;line-height:1.55}
  .about p{margin-bottom:5px}
  .about strong{color:var(--ink)}
  .callout{position:absolute;left:30px;right:30px;font-family:"Saira Condensed",sans-serif;font-weight:700;font-size:25px;line-height:1.15;color:var(--ink);text-align:center}
  .page--left .callout{top:608px}
  .page--right .callout{top:668px}
  .url-pill{position:absolute;left:50%;transform:translateX(-50%);top:712px;padding:11px 30px;border-radius:30px;background:linear-gradient(90deg,var(--teal),var(--blue));color:#fff;font-family:"Saira Condensed",sans-serif;font-weight:600;font-size:19px;letter-spacing:.8px;white-space:nowrap}
  .packages{position:absolute;left:46px;right:40px;top:362px;font-size:9.6px;line-height:1.5;list-style:none}
  .packages li{margin-bottom:6px}
  .packages strong{color:var(--ink)}
</style>
</head>
<body>
<main class="spread">

  <section class="page page--left">
    <svg class="page__art" viewBox="0 0 518 800" preserveAspectRatio="none" aria-hidden="true">
      <defs>
        <linearGradient id="headerWash" x1="0" y1="0" x2="0" y2="1">
          <stop offset="0" stop-color="#eef2f4"/>
          <stop offset="1" stop-color="#E9F6FB"/>
        </linearGradient>
        <linearGradient id="bandGrad" x1="0" y1="0" x2="1" y2="0">
          <stop offset="0" stop-color="#00BBA5"/>
          <stop offset="1" stop-color="#00A9DD"/>
        </linearGradient>
      </defs>
      <path d="M0 0H518V250C420 200 250 190 0 220Z" fill="url(#headerWash)"/>
      <path d="M0 220C250 190 420 200 518 250V270C420 225 250 215 0 240Z" fill="#C7EBF8" opacity=".8"/>
      <path d="M0 240C250 215 420 225 518 270V282C420 240 250 232 0 252Z" fill="#E9F6FB"/>
      <rect x="0" y="0" width="518" height="5" fill="url(#bandGrad)"/>
      <path d="M0 770C150 755 350 760 518 790V800H0Z" fill="url(#bandGrad)"/>
    </svg>

    <h1 class="page__title"><span class="accent">About</span> Us</h1>
    <span class="page__number">01</span>

    <div class="brand">
      <div class="brand__row">
        <span class="brand__dot"></span>
        <span class="brand__name">Swift Renewal</span>
      </div>
      <span class="brand__tagline">Feel Well Sooner</span>
    </div>

    <div class="about">
      <p><strong>Swift Renewal</strong> - opened in Riverbend, Louisiana in 2017 and was soon drawing patients from across Louisiana, Arkansas, and Texas.</p>
      <p>The vision of our owners (Dan and Mira) has always been to provide safe, quality IV treatment in an inviting environment that doesn't carry the stigma of a medical facility.</p>
      <p>There's no waiting in a crowded lobby, no one next to you with a broken arm or violent cough, and no surprise bill will come.</p>
      <p>That doesn't mean you aren't getting excellent care. Our Medical Director is always available for consultation, and our nurses all have a minimum of five years extensive IV experience.</p>
      <p>The goal has always been to help you Feel Well Sooner. If you can do that while sitting in a leather recliner, sipping a fruit juice, watching television, and relaxing while you're being treated, we say "all the better".</p>
      <p>Give us an hour, and we will get you back on your game.</p>
    </div>

    <p class="callout">Call 855.555.0142 to book a Housecall or<br>Afterhours appointment</p>
    <span class="url-pill">www.swiftrenewalroom.com/treatments</span>
  </section>

  <section class="page page--right">
    <svg class="page__art" viewBox="0 0 518 800" preserveAspectRatio="none" aria-hidden="true">
      <defs>
        <linearGradient id="bandGradR" x1="0" y1="0" x2="1" y2="0">
          <stop offset="0" stop-color="#00BBA5"/>
          <stop offset="1" stop-color="#00A9DD"/>
        </linearGradient>
      </defs>
      <rect x="0" y="0" width="518" height="5" fill="url(#bandGradR)"/>
      <path d="M0 770C150 755 350 760 518 790V800H0Z" fill="url(#bandGradR)"/>
    </svg>

    <svg class="page__art" viewBox="0 0 518 800" preserveAspectRatio="none" role="img" aria-label="Photo of IV drip bags filled with fresh fruit on a teal background">
      <defs>
        <linearGradient id="photoTone" x1="0" y1="0" x2="1" y2="1">
          <stop offset="0" stop-color="#67D7C9"/>
          <stop offset=".6" stop-color="#4fc3c0"/>
          <stop offset="1" stop-color="#8fdad3"/>
        </linearGradient>
      </defs>
      <path d="M0 100H518V320C400 290 230 285 0 330Z" fill="url(#photoTone)"/>
      <path d="M0 330C230 285 400 290 518 320V336C400 306 230 302 0 346Z" fill="#C7EBF8"/>
    </svg>

    <h1 class="page__title"><span class="accent">IV</span> Packages</h1>
    <span class="page__number">02</span>

    <ul class="packages">
      <li><strong>The Baseline</strong> - A full liter of Ringer's Lactate, a balanced fluid perfect for simple dehydration and exhaustion.</li>
      <li><strong>The Extra Drop</strong> - "A little something extra". A liter of Ringer's Lactate infused with Magnesium, Thiamine, Folic Acid, and a powerful multivitamin. When you need "a little more" than fluids.</li>
      <li><strong>The Headliner</strong> - Everything above plus a strong pain reliever, an anti-nausea med, and 30 minutes of medical oxygen. If this doesn't end your hangover, you need to stop going out.</li>
      <li><strong>The Tummy Reset</strong> - Replaces the fluids and nutrients you've lost, stops the nausea, and keeps you from losing any more lunch.</li>
      <li><strong>Head Calm</strong> - Puts a quick stop to your pain. A cool, quiet room, a comfy lounger, and an IV with a pain reliever, muscle tension relieving magnesium, medical oxygen and other vasodilators.</li>
      <li><strong>The Power Play</strong> - Contains a proprietary blend of amino acids (AMB) which boosts metabolism before, and promotes muscle healing after, intense physical activity.</li>
    </ul>

    <p class="callout">More IV Packages can be found at</p>
    <span class="url-pill">www.swiftrenewalroom.com/treatments</span>
  </section>

</main>
</body>
</html>
```